Revamp Business Card for Landscaping/Gardening Service Provider

We are a small landscaping company that is in desperate need of someone to recreate our business card. I have attached what we are currently using along with the logo.

These are the services we specialize in:
- lawn service
- mow, edge and clean
- fertilizing
- prune and trim
- seed and topping
- planting
- irrigation sprinklers

We don't want the front to be too busy but we do want the bulk of the information to be on this side such as the logo (recreate if possible), what we do and maybe the contact information. The back we would like it to be lined if possible, to add notes or even provide quotes for customers. If you feel you've got the talent to take on this project, please send in your design.

Thank you

```html
<!DOCTYPE html>
<html lang="en">
<head>
<meta charset="UTF-8">
<title>Rivera Green Gardening – Business Card</title>
<link href="https://fonts.googleapis.com/css2?family=Roboto+Condensed:wght@400;700&family=Great+Vibes&display=swap" rel="stylesheet">
<style>
  :root {
    --stage: #2a2d31;
    --leaf: #3f6b2a;
    --leaf-dark: #2f5420;
    --grass-light: #8cc63f;
    --grass-mid: #4e8a2a;
    --grass-deep: #1f3f14;
    --slate: #5f6468;
    --slate-dark: #3a3e41;
    --paper: #eef0ea;
    --ink: #3d4a33;
    --rule: #8a9482;
    --white: #ffffff;
  }
  * { box-sizing: border-box; margin: 0; padding: 0; }
  html, body { width: 1200px; height: 900px; overflow: hidden; }
  body {
    background: var(--stage);
    font-family: "Roboto Condensed", Arial, sans-serif;
    position: relative;
  }
  .card {
    position: absolute;
    left: 240px;
    width: 720px;
    height: 411px;
    overflow: hidden;
    box-shadow: 0 10px 30px rgba(0,0,0,.45);
  }
  .card--front { top: 26px; background: var(--slate-dark); }
  .card--back { top: 463px; }

  /* ---------- front ---------- */
  .grass-photo {
    position: absolute; left: 0; top: 0; width: 430px; height: 100%;
    background:
      radial-gradient(ellipse at 55% 30%, rgba(200,230,140,.55), transparent 55%),
      linear-gradient(175deg, var(--grass-light) 0%, var(--grass-mid) 45%, var(--grass-deep) 100%);
  }
  .slate-panel {
    position: absolute; right: 0; top: 0; width: 420px; height: 100%;
    background: linear-gradient(160deg, var(--slate) 0%, var(--slate-dark) 100%);
    clip-path: polygon(18% 0, 100% 0, 100% 100%, 0 100%);
  }
  .contact-band {
    position: absolute; left: 0; top: 0; width: 100%; height: 52px;
    background: rgba(255,255,255,.92);
  }
  .ribbon {
    position: absolute;
    background: var(--leaf);
    color: var(--white);
    clip-path: polygon(0 0, calc(100% - 18px) 0, 100% 50%, calc(100% - 18px) 100%, 0 100%);
    display: flex; align-items: center; gap: 8px;
    padding: 0 26px 0 14px;
    height: 30px;
    font-size: 14px; letter-spacing: .5px;
    white-space: nowrap;
  }
  .ribbon--name { left: 430px; top: 11px; font-weight: 700; font-size: 15px; letter-spacing: 1.5px; background: var(--leaf-dark); }
  .ribbon--phone { left: 0; top: 66px; }
  .ribbon--mail { left: 0; top: 104px; }
  .ribbon--web { left: 0; top: 142px; }
  .ribbon svg { width: 14px; height: 14px; flex: none; }
  .accent-lines { position: absolute; left: 20px; top: 14px; }

  .brand-mark {
    position: absolute; left: 470px; top: 68px;
    width: 150px; height: 120px;
    border: 2px solid var(--white);
    display: flex; flex-direction: column; align-items: center; justify-content: center;
    color: var(--white);
    font-weight: 700; font-size: 19px; letter-spacing: 2px; line-height: 1.15; text-align: center;
  }
  .services {
    position: absolute; left: 440px; top: 210px;
    list-style: none;
    color: var(--white);
    font-size: 22px; line-height: 27px;
  }
  .services li { display: flex; align-items: center; gap: 10px; }
  .services li::before {
    content: ""; width: 10px; height: 10px; border-radius: 50%;
    background: var(--white); flex: none;
  }

  /* ---------- back ---------- */
  .garden-photo {
    position: absolute; inset: 0;
    background:
      radial-gradient(circle at 80% 75%, rgba(150,50,40,.75), transparent 25%),
      radial-gradient(circle at 15% 20%, rgba(220,120,150,.55), transparent 18%),
      radial-gradient(circle at 92% 30%, rgba(170,90,60,.6), transparent 20%),
      linear-gradient(165deg, #6d8f45 0%, #3f6a2a 45%, #5a7a3a 70%, #2d4a1e 100%);
  }
  .notes-panel {
    position: absolute; left: 0; top: 96px; width: 470px; height: 315px;
    background: var(--paper);
    clip-path: polygon(0 0, 100% 0, 92% 100%, 0 100%);
    padding: 22px 80px 0 28px;
  }
  .notes-title {
    font-family: "Great Vibes", cursive;
    color: var(--ink);
    font-size: 30px;
    line-height: 40px;
    white-space: nowrap;
    padding-left: 30px;
    margin-bottom: 4px;
  }
  .notes-line {
    border-bottom: 2px dotted var(--rule);
    height: 38px;
  }
  .brand-tile {
    position: absolute; left: 390px; top: 38px;
    width: 180px; height: 180px;
    background: var(--leaf);
    padding: 10px;
  }
  .brand-tile__frame {
    width: 100%; height: 100%;
    border: 2px solid var(--white);
    display: flex; flex-direction: column; align-items: center; justify-content: center;
    color: var(--white);
    font-weight: 700; font-size: 21px; letter-spacing: 2px; line-height: 1.15; text-align: center;
  }
</style>
</head>
<body>

<section class="card card--front" aria-label="Business card front">
  <div class="grass-photo" role="img" aria-label="Close-up photo of fresh green lawn grass"></div>
  <div class="slate-panel"></div>
  <div class="contact-band"></div>
  <svg class="accent-lines" width="120" height="26" viewBox="0 0 120 26" aria-hidden="true">
    <line x1="0" y1="6" x2="110" y2="6" stroke="#3f6b2a" stroke-width="3"/>
    <line x1="0" y1="13" x2="110" y2="13" stroke="#3f6b2a" stroke-width="3"/>
    <line x1="0" y1="20" x2="110" y2="20" stroke="#3f6b2a" stroke-width="3"/>
  </svg>

  <div class="ribbon ribbon--name">TOMAS &amp; ELENA RIVERA</div>
  <div class="ribbon ribbon--phone">
    <svg viewBox="0 0 24 24" aria-hidden="true"><path fill="#fff" d="M6.6 10.8a15 15 0 0 0 6.6 6.6l2.2-2.2c.3-.3.7-.4 1-.2 1.1.4 2.3.6 3.6.6.6 0 1 .4 1 1V20c0 .6-.4 1-1 1A17 17 0 0 1 3 4c0-.6.4-1 1-1h3.5c.6 0 1 .4 1 1 0 1.3.2 2.5.6 3.6.1.3 0 .7-.2 1z"/></svg>
    555.014.2290
  </div>
  <div class="ribbon ribbon--mail">
    <svg viewBox="0 0 24 24" aria-hidden="true"><rect x="2" y="5" width="20" height="14" rx="2" fill="#fff"/><path d="M3 6l9 7 9-7" stroke="#3f6b2a" stroke-width="2" fill="none"/></svg>
    info@riveragreen.com
  </div>
  <div class="ribbon ribbon--web">
    <svg viewBox="0 0 24 24" aria-hidden="true"><circle cx="12" cy="12" r="9" fill="none" stroke="#fff" stroke-width="2"/><path d="M3 12h18M12 3c3 3 3 15 0 18M12 3c-3 3-3 15 0 18" stroke="#fff" stroke-width="1.5" fill="none"/></svg>
    www.riveragreen.com
  </div>

  <div class="brand-mark"><span>RIVERA GREEN</span><span>GARDENING</span></div>

  <ul class="services">
    <li>lawn service</li>
    <li>mow, edge and clean</li>
    <li>fertilizing</li>
    <li>prune and trim</li>
    <li>seed and topping</li>
    <li>planting</li>
    <li>irrigation sprinklers</li>
  </ul>
</section>

<section class="card card--back" aria-label="Business card back">
  <div class="garden-photo" role="img" aria-label="Photo of a planted garden bed with shrubs and flowers"></div>
  <div class="notes-panel">
    <p class="notes-title">“Quotation &amp; Notes”</p>
    <div class="notes-line"></div>
    <div class="notes-line"></div>
    <div class="notes-line"></div>
    <div class="notes-line"></div>
    <div class="notes-line"></div>
    <div class="notes-line"></div>
  </div>
  <div class="brand-tile">
    <div class="brand-tile__frame"><span>RIVERA GREEN</span><span>GARDENING</span></div>
  </div>
</section>

</body>
</html>
```